Corvella Paintless Dent Removal

Our company works on vehicles removing dents using a highly skilled trade which the metal is massaged out with special tools without disturbing the original paint, hence paintless dent removal. Besides keeping the paint and metal original its also very environmentally friendly since no paint or toxic fillers are used. Also we we are one of the most experienced companies in the business with 25 years

Target Market(s)

Retail Automobile consumers, Auto Dealerships and Auto Body Shops

Industry/Entity Type

Auto Repair

Contact Information for Business Card

Dennis Holbrook
PO Box 538 Ashmere, NY 11952
631-472-8816
corvellapdr@mailnest.example
website corvellapdr.example
youtube corvella paintless dent removal
25 years of experience removing Dents, Dings and Hail Damage

Font styles to use
Serif
Sans Serif

Colors

Designer to choose colors to be used in the design.

Requirements
Must have
• I do like things that are simple but classy and somewhat bold, also I like my logo so that should be somewhat important

```html
<!DOCTYPE html>
<html lang="en">
<head>
<meta charset="utf-8">
<title>Corvella Paintless Dent Removal – Business Card</title>
<link rel="stylesheet" href="https://fonts.googleapis.com/css2?family=Roboto:wght@400;500;700&display=swap">
<style>
  :root {
    --navy: #13254a;
    --navy-deep: #0f2149;
    --green: #6bb42a;
    --paper: #f4f4f4;
    --paper-shade: #e2e2e2;
    --ground: #c7c7c7;
    --ink: #1b2a4e;
    --muted: #d6dbe6;
  }
  * { box-sizing: border-box; margin: 0; padding: 0; }
  html, body { width: 1200px; height: 576px; overflow: hidden; }
  body {
    background: var(--ground);
    font-family: "Roboto", Arial, sans-serif;
    position: relative;
  }
  .card {
    position: absolute;
    top: 138px;
    width: 485px;
    height: 294px;
    border-radius: 11px;
    overflow: hidden;
  }
  /* Front */
  .card-front {
    left: 82px;
    background: var(--navy);
  }
  .front-brand {
    position: absolute;
    left: 0; right: 0; top: 88px;
    text-align: center;
    color: #ffffff;
    font-weight: 700;
    font-size: 34px;
    line-height: 1.15;
    letter-spacing: 0.5px;
  }
  .front-brand .brand-line-sub { font-size: 20px; display: block; }
  .front-web {
    position: absolute;
    left: 0; right: 0; top: 262px;
    display: flex; align-items: center; justify-content: center; gap: 18px;
    color: var(--muted);
    font-size: 12.5px;
    letter-spacing: 0.8px;
  }
  .front-web .accent { color: var(--green); }
  .front-web .rule {
    width: 92px; height: 2px;
    background: linear-gradient(90deg, transparent, var(--green) 40%);
  }
  .front-web .rule.right { background: linear-gradient(270deg, transparent, var(--green) 40%); }

  /* Back */
  .card-back {
    left: 602px;
    background: linear-gradient(135deg, #fbfbfb 0%, var(--paper) 55%, var(--paper-shade) 100%);
    color: var(--ink);
  }
  .back-brand {
    position: absolute;
    left: 24px; top: 42px;
    display: flex; align-items: center; gap: 10px;
    color: var(--navy);
    font-weight: 700;
    font-size: 21px;
    letter-spacing: 0.3px;
  }
  .back-brand .mark {
    width: 14px; height: 14px; border-radius: 50%;
    background: var(--green);
  }
  .holder-name {
    position: absolute; left: 24px; top: 157px;
    font-size: 21px; font-weight: 700; color: var(--navy);
  }
  .holder-title {
    position: absolute; left: 24px; top: 184px;
    font-size: 11.5px; color: var(--ink);
  }
  .experience {
    position: absolute; left: 24px; top: 228px;
    font-size: 11.5px; line-height: 14px; color: var(--ink);
  }
  .contact {
    position: absolute; left: 262px; top: 162px;
    font-size: 11.5px; color: var(--ink);
    line-height: 16px;
  }
  .contact .address { margin-bottom: 4px; }
  .contact-list { list-style: none; }
  .contact-list li { display: flex; align-items: center; gap: 14px; height: 17px; }
  .contact-list svg { width: 10px; height: 10px; flex: none; }
  .band-green {
    position: absolute; left: 0; bottom: 0;
    width: 240px; height: 13px;
    background: var(--green);
  }
  .band-navy {
    position: absolute; right: 0; bottom: 0;
    width: 259px; height: 29px;
    background: var(--navy-deep);
    clip-path: polygon(14px 0, 100% 0, 100% 100%, 0 100%);
    display: flex; align-items: center; gap: 12px;
    padding-left: 38px;
    color: #ffffff; font-size: 11.5px;
  }
  .band-navy .video-square {
    width: 12px; height: 10px; background: #ffffff; border-radius: 2px;
  }
</style>
</head>
<body>
  <section class="card card-front" aria-label="Card front">
    <div class="front-brand">Corvella<span class="brand-line-sub">Paintless Dent Removal</span></div>
    <div class="front-web">
      <span class="rule"></span>
      <span>www.<span class="accent">corvellapdr</span>.example</span>
      <span class="rule right"></span>
    </div>
  </section>

  <section class="card card-back" aria-label="Card back">
    <div class="back-brand"><span class="mark"></span>Corvella Paintless Dent Removal</div>

    <h1 class="holder-name">Dennis Holbrook</h1>
    <p class="holder-title">Managing Director</p>
    <p class="experience">25 years of experience removing<br>Dents, Dings and Hail Damage</p>

    <div class="contact">
      <p class="address">PO Box 538 Ashmere,<br>NY 11952</p>
      <ul class="contact-list">
        <li>
          <svg viewBox="0 0 10 10" aria-hidden="true"><path fill="#6bb42a" d="M1 3.2C1 2 2 1.5 5 1.5S9 2 9 3.2L7.6 3.6 7 2.8H3L2.4 3.6zM2.5 4.5h5L8.5 9h-7z"/></svg>
          <span>631-472-8816</span>
        </li>
        <li>
          <svg viewBox="0 0 10 10" aria-hidden="true"><rect x="0.5" y="2" width="9" height="6.5" fill="#6bb42a"/><path d="M0.5 2 5 5.6 9.5 2" fill="none" stroke="#ffffff" stroke-width="0.9"/></svg>
          <span>corvellapdr@mailnest.example</span>
        </li>
        <li>
          <svg viewBox="0 0 10 10" aria-hidden="true"><circle cx="5" cy="5" r="4.3" fill="#6bb42a"/><path d="M0.7 5h8.6M5 0.7c-2.4 2.6-2.4 6 0 8.6M5 0.7c2.4 2.6 2.4 6 0 8.6" fill="none" stroke="#ffffff" stroke-width="0.6"/></svg>
          <span>www.corvellapdr.example</span>
        </li>
      </ul>
    </div>

    <div class="band-green"></div>
    <div class="band-navy"><span class="video-square"></span><span>videohub.example/Dennis Holbrook</span></div>
  </section>
</body>
</html>
```